IT Consulting company Needs a Logo Design and Business Cards

I need a New Logo and Business Cards for an established IT Managed Services Company that specializes in flat-rate managed IT services. We provide Design and Build, Help Desk, Onsite and Remote Support Services.

Target Market(s)

Corporate Clients

Industry/Entity Type

It Company

Logo Text

Halvern Systems Collective

Requirements
Nice to have
• Tag Line= Technology at Lightning Speed

```html
<!DOCTYPE html>
<html lang="en">
<head>
<meta charset="UTF-8">
<title>Halvern Systems Collective – Business Cards</title>
<link href="https://fonts.googleapis.com/css2?family=Montserrat:wght@400;500&family=Oswald:wght@500&display=swap" rel="stylesheet">
<style>
  :root {
    --backdrop: #161616;
    --card: #222222;
    --card-edge: #2a2a2a;
    --brand-blue: #2d43b3;
    --text-light: #f2f2f2;
  }
  * { margin: 0; padding: 0; box-sizing: border-box; }
  html, body {
    width: 1200px; height: 900px; overflow: hidden;
    background: var(--backdrop);
  }
  .canvas {
    position: relative; width: 1200px; height: 900px;
    display: flex; flex-direction: column; align-items: center; justify-content: center; gap: 48px;
  }
  .card {
    position: relative; width: 580px; height: 330px;
    background: linear-gradient(135deg, var(--card) 0%, var(--card-edge) 100%);
    border-bottom: 6px solid var(--brand-blue);
    box-shadow: 0 12px 30px rgba(0,0,0,0.55);
  }
  .card-front { display: flex; align-items: center; justify-content: center; padding-bottom: 40px; }
  .brand-name {
    font-family: "Montserrat", sans-serif; font-weight: 500;
    font-size: 33px; color: var(--brand-blue); letter-spacing: 0.5px;
  }
  .card-back { display: flex; align-items: center; padding-left: 56px; }
  .person { text-align: right; }
  .person-name {
    font-family: "Oswald", sans-serif; font-weight: 500;
    font-size: 42px; line-height: 1; color: var(--brand-blue); text-transform: uppercase; letter-spacing: 0.5px;
  }
  .person-role {
    margin-top: 8px;
    font-family: "Montserrat", sans-serif; font-size: 17px; color: var(--text-light);
  }
  .divider { width: 2px; height: 78px; background: var(--brand-blue); margin: 0 26px 0 30px; }
  .contact-list { list-style: none; }
  .contact-item {
    display: flex; align-items: center; gap: 12px;
    font-family: "Montserrat", sans-serif; font-size: 17px; color: var(--text-light); line-height: 28px;
  }
  .contact-icon { width: 13px; height: 13px; flex: none; }
</style>
</head>
<body>
<main class="canvas">
  <section class="card card-front">
    <div class="brand-name">Halvern Systems Collective</div>
  </section>

  <section class="card card-back">
    <div class="person">
      <div class="person-name">Dana Whitlow</div>
      <div class="person-role">Director</div>
    </div>
    <div class="divider"></div>
    <ul class="contact-list">
      <li class="contact-item">
        <svg class="contact-icon" viewBox="0 0 16 16" aria-hidden="true"><path d="M4 1.5 6.2 5 4.8 6.6c.9 2 2.5 3.6 4.6 4.6L11 9.8l3.5 2.2-1 2.5C7.6 14.2 1.8 8.4 1.5 2.5z" fill="var(--brand-blue)"/></svg>
        +331 5820 4419
      </li>
      <li class="contact-item">
        <svg class="contact-icon" viewBox="0 0 16 16" aria-hidden="true"><rect x="1.5" y="3.5" width="13" height="9" fill="none" stroke="var(--brand-blue)" stroke-width="1.4"/><path d="M1.5 3.5 8 9l6.5-5.5" fill="none" stroke="var(--brand-blue)" stroke-width="1.4"/></svg>
        info@halvern.com
      </li>
      <li class="contact-item">
        <svg class="contact-icon" viewBox="0 0 16 16" aria-hidden="true"><circle cx="8" cy="8" r="6.3" fill="none" stroke="var(--brand-blue)" stroke-width="1.3"/><ellipse cx="8" cy="8" rx="2.8" ry="6.3" fill="none" stroke="var(--brand-blue)" stroke-width="1.1"/><path d="M1.7 8h12.6" stroke="var(--brand-blue)" stroke-width="1.1"/></svg>
        www.halvern.com
      </li>
    </ul>
  </section>
</main>
</body>
</html>
```